Brightway Rug and Floor cleaning Business card Design

I need a design that has the same feel as my van.
i would also like a prominent "Review us on facebook" somewhere, but not that it makes it look silly.
I would like the card to have a little bit of grey or black in the design as well.

It will need contact details
phone: 0498 276154
email: rkbrightwayfloors@mailbox-example.com
website: www.brightwayrugandfloorcleaning-example.com.au
facebook: /brightwayrugandfloorcleaning

Industry/Entity Type

Business

Contact Information for Business Card

Phone number 0498276154
Email rkbrightwayfloors@mailbox-example.com
Website www.brightwayrugandfloorcleaning-example.com.au
Facebook/brightwayrugandfloorcleaning

Colors
000000

Requirements
Must have
• Same feel as my van
• I want the card to stand out from the crowd
Nice to have
• Maybe include a tiny bit of a third colour? Grey's,blacks, orange?

```html
<!DOCTYPE html>
<html lang="en">
<head>
<meta charset="utf-8">
<title>Brightway Rug and Floor Cleaning – Business Card</title>
<link href="https://fonts.googleapis.com/css2?family=Open+Sans:wght@400;700&display=swap" rel="stylesheet">
<style>
  :root {
    --backdrop: #e9e6e3;
    --card-blue: #00aedb;
    --card-grey: #6b6e72;
    --text-white: #ffffff;
    --accent-sky: #8fdcf0;
    --name-sky: #4cc6ea;
  }
  * { margin: 0; padding: 0; box-sizing: border-box; }
  html, body {
    width: 1200px; height: 900px; overflow: hidden;
    background: var(--backdrop);
    font-family: "Open Sans", Arial, sans-serif;
  }
  .canvas { position: relative; width: 1200px; height: 900px; }
  .card {
    position: absolute; height: 342px;
    box-shadow: 0 6px 18px rgba(0,0,0,0.18);
  }
  .card--front { left: 238px; top: 62px; width: 555px; background: var(--card-blue); }
  .card--back { left: 459px; top: 518px; width: 559px; height: 343px; background: var(--card-grey); }

  .brand {
    position: absolute; left: 0; right: 0;
    display: flex; align-items: center; justify-content: center; gap: 10px;
  }
  .card--front .brand { top: 112px; }
  .card--back .brand { top: 130px; }
  .brand__dot { width: 14px; height: 14px; border-radius: 50%; flex: none; }
  .brand__name {
    font-weight: 700; font-size: 25px; line-height: 1.2;
    text-align: center; white-space: nowrap;
  }
  .card--front .brand__name { color: var(--text-white); }
  .card--front .brand__dot { background: var(--text-white); }
  .card--back .brand__name { color: var(--name-sky); }
  .card--back .brand__dot { background: var(--name-sky); }

  .contact-list {
    position: absolute; left: 0; right: 0; top: 203px;
    list-style: none; color: var(--text-white);
    font-size: 14.5px; line-height: 23px; text-align: center;
  }
  .contact-list li { display: flex; align-items: center; justify-content: center; gap: 7px; white-space: nowrap; }
  .contact-list svg { width: 12px; height: 12px; fill: var(--text-white); flex: none; }
  .icon-square { width: 11px; height: 11px; background: var(--text-white); border-radius: 2px; flex: none; }

  .promo {
    position: absolute; left: 0; right: 0; top: 238px;
    text-align: center; color: var(--accent-sky); font-size: 16px; white-space: nowrap;
  }
</style>
</head>
<body>
<main class="canvas">
  <section class="card card--front" aria-label="Business card front">
    <div class="brand">
      <span class="brand__dot"></span>
      <span class="brand__name">Brightway Rug and Floor Cleaning</span>
    </div>
    <ul class="contact-list">
      <li>
        <svg viewBox="0 0 24 24" aria-hidden="true"><path d="M6.6 10.8a15.1 15.1 0 0 0 6.6 6.6l2.2-2.2c.3-.3.7-.4 1-.2 1.1.4 2.3.6 3.6.6.6 0 1 .4 1 1V20c0 .6-.4 1-1 1A17 17 0 0 1 3 4c0-.6.4-1 1-1h3.5c.6 0 1 .4 1 1 0 1.3.2 2.5.6 3.6.1.3 0 .7-.2 1z"/></svg>
        0498 276154
      </li>
      <li>
        <svg viewBox="0 0 24 24" aria-hidden="true"><path d="M2 5h20v14H2z M3.5 6.5 12 13l8.5-6.5" fill="none" stroke="#fff" stroke-width="2"/><path d="M2 5h20v2l-10 7L2 7z"/></svg>
        rkbrightwayfloors@mailbox-example.com
      </li>
      <li>
        <svg viewBox="0 0 24 24" aria-hidden="true"><circle cx="12" cy="12" r="9" fill="none" stroke="#fff" stroke-width="2.4"/><path d="M3 12h18M12 3c3 3 3 15 0 18M12 3c-3 3-3 15 0 18" fill="none" stroke="#fff" stroke-width="1.8"/></svg>
        brightwayrugandfloorcleaning-example.com.au
      </li>
      <li>
        <span class="icon-square" aria-hidden="true"></span>
        /brightwayrugandfloorcleaning
      </li>
    </ul>
  </section>

  <section class="card card--back" aria-label="Business card back">
    <div class="brand">
      <span class="brand__dot"></span>
      <span class="brand__name">Brightway Rug and Floor Cleaning</span>
    </div>
    <p class="promo">Win Carpet Cleaning For YOU and a FRIEND!</p>
  </section>
</main>
</body>
</html>
```